Tender Horizon yoga, meditation & wellness

I teach kundalini yoga and meditation classes.
I have adult beginner classes, seniors classes, family yoga classes, kids yoga classes
I also offer events like cacao ceremony, full moon ceremony, and retreats

Professional, and simple website that is easy to navigate, and easy for me to update, change.

Target Market(s)

all ages

Industry/Entity Type

Health And Wellness

Coding

Coded - Design and coding required

Number of Pages Required

5+ page

Font styles to use
Decorative

Colors
cedeed
eedded
e4daeb
fbd4d5
fee3d4

Requirements
Must have
• tabs required: about, contact, events, classes, blog,
• I would like to link my facebook page & instagram accounts to the website
Nice to have
• I would like my clients to be able to register for classes and events from my website
• I would like to have a "shop" option in the future, for some items that I have for sale

```html
<!DOCTYPE html>
<html lang="en">
<head>
<meta charset="utf-8">
<title>Tender Horizon — Kundalini Yoga</title>
<link rel="stylesheet" href="https://fonts.googleapis.com/css2?family=Poppins:wght@200;300;400;500;600;700&display=swap">
<style>
:root{
  --blue:#cedeed;
  --blush:#eedded;
  --lavender:#e4daeb;
  --pink:#fbd4d5;
  --peach:#fee3d4;
  --ink:#3b3b3d;
  --body:#5c5c60;
  --muted:#7a7a80;
  --violet:#a58bb3;
  --panel:#ffffff;
  --hero-dark:#2e3136;
  --section-blue:#dbe2ea;
  --section-grey:#ececef;
  --card-blue:#c7d3e1;
  --card-pink:#f1cdd0;
  --card-peach:#f3d3c6;
  --btn-dark:#3f3f42;
}
*{box-sizing:border-box;margin:0;padding:0}
html,body{width:1200px;height:4186px;overflow:hidden}
body{font-family:'Poppins',sans-serif;color:var(--body);background:#fff;position:relative}
.abs{position:absolute}
p{font-size:13px;line-height:1.75;font-weight:400}
h2{font-family:'Poppins',sans-serif;font-weight:600;color:var(--ink);font-size:38px;line-height:1.2}

/* Hero */
.hero{left:0;top:0;width:1200px;height:698px;overflow:hidden;
  background:radial-gradient(ellipse 420px 260px at 860px 250px,rgba(214,170,130,.55),transparent 70%),
  linear-gradient(180deg,#4c5058 0%,#5d5f64 38%,#3a3c40 62%,var(--hero-dark) 100%)}
.hero-ridge{left:0;top:380px;width:1200px;height:318px;background:linear-gradient(180deg,rgba(30,32,36,0) 0%,rgba(30,32,36,.75) 60%)}
.brand{left:92px;top:30px;display:flex;align-items:center;gap:12px;color:#fff;font-size:24px;font-weight:400;letter-spacing:.5px}
.brand-mark{width:30px;height:30px;border:2px solid #fff;border-radius:50%}
.hero-circle{left:484px;top:36px;width:236px;height:236px;border-radius:50%;background:#b9c6d6;opacity:.9}
.hero-kicker{left:0;top:330px;width:1200px;text-align:center;color:rgba(255,255,255,.85);font-weight:200;font-size:52px;letter-spacing:.22em}
.hero-title{left:0;top:398px;width:1200px;text-align:center;color:rgba(255,255,255,.9);font-weight:700;font-size:54px;letter-spacing:.2em}
.portrait{left:441px;top:536px;width:318px;height:335px;border:5px solid #4a4a4d;background:#fff;box-shadow:0 6px 18px rgba(0,0,0,.3)}
.portrait-photo{width:100%;height:276px;background:linear-gradient(180deg,#e7e4e1 0%,#c9b8a8 55%,#a9714f 100%)}
.portrait-caption{height:49px;background:#5a5a5e;color:#fff;font-size:15px;font-weight:500;text-align:center;line-height:49px;letter-spacing:.5px}

/* Menu panel */
.menu{left:818px;top:0;width:382px;height:614px;background:var(--panel);box-shadow:0 6px 20px rgba(0,0,0,.15);z-index:5}
.menu-close{position:absolute;left:250px;top:33px;width:40px;height:40px;border:1px solid #9a9a9f;color:#6b6b70;font-size:26px;font-weight:300;text-align:center;line-height:38px}
.menu-list{position:absolute;left:61px;top:68px;list-style:none}
.menu-list li{font-size:16px;font-weight:400;color:#2f2f32;height:77.5px;letter-spacing:.3px}
.menu-social{position:absolute;left:61px;top:520px;display:flex;gap:20px}
.menu-social span{width:27px;height:27px;background:#8f8f95}
.menu-social span:first-child{background:var(--pink)}

/* Features */
.feature{top:753px;display:flex;gap:24px;width:330px}
.feature-icon{width:84px;height:100px;flex:none;border-radius:4px}
.feature h3{font-size:19px;font-weight:600;color:var(--ink);margin:4px 0 6px}
.feature p{font-size:11.5px;line-height:1.6;color:var(--muted)}

/* Kundalini section */
.intro{left:0;top:940px;width:1200px;height:1097px;background:var(--section-blue)}
.intro-photo{left:0;top:0;width:502px;height:617px;background:linear-gradient(170deg,#8a988a 0%,#4f5e50 45%,#dcdcdc 75%,#2f3a4c 100%)}
.intro-copy{left:530px;top:84px;width:600px}
.intro-copy h2{font-size:36px;font-weight:500;margin-bottom:26px}
.intro-copy p{font-size:11.5px;margin-bottom:14px}
.wellbeing-photo{left:740px;top:455px;width:460px;height:642px;background:linear-gradient(180deg,#e9edf1 0%,#d4d4d6 40%,#b0805f 70%,#e4e6ea 100%)}
.wellbeing-copy{left:84px;top:690px;width:600px}
.wellbeing-copy h2{margin-bottom:22px}
.wellbeing-copy p{font-size:11.5px;margin-bottom:14px}
.btn{display:inline-block;border:2px solid var(--btn-dark);color:var(--ink);font-size:15px;font-weight:500;padding:0 24px;height:46px;line-height:42px}

/* Contribute section */
.contribute{left:0;top:2050px;width:1200px;height:650px;background:var(--section-grey)}
.stack{left:126px;top:84px;width:585px;height:430px}
.stack-back{position:absolute;background:#fff;box-shadow:0 3px 10px rgba(0,0,0,.18);border:12px solid #fff}
.stack-back.one{left:30px;top:-20px;width:560px;height:410px;transform:rotate(5deg);background:#d8d8d8}
.stack-back.two{left:20px;top:-8px;width:560px;height:410px;transform:rotate(2deg);background:#cfcfcf}
.stack-front{position:absolute;left:0;top:10px;width:572px;height:400px;border:12px solid #fff;box-shadow:0 4px 14px rgba(0,0,0,.25);transform:rotate(-2deg);background:linear-gradient(180deg,#5c6d48 0%,#7c8c5a 45%,#6e7a4a 70%,#8a8f66 100%)}
.contribute-copy{left:790px;top:70px;width:340px}
.contribute-copy h2{margin-bottom:20px}
.contribute-copy p{font-size:11.5px;margin-bottom:28px}

/* Classes section */
.classes{left:0;top:2706px;width:1200px;height:642px;background:linear-gradient(90deg,var(--lavender) 0%,#e8dbe4 60%,var(--blush) 100%)}
.classes-copy{left:84px;top:70px;width:470px}
.classes-copy h2{margin-bottom:22px}
.classes-copy p{font-size:11.5px}
.class-list{left:84px;top:315px;width:470px;list-style:none}
.class-item{display:flex;gap:20px;height:84px;border-bottom:1px solid rgba(150,130,160,.35);padding-top:14px}
.class-item:last-child{border-bottom:none}
.class-item svg{flex:none}
.class-item h4{font-size:15px;font-weight:600;color:var(--ink)}
.class-item span{font-size:14px;color:var(--body)}
.classes-photo{left:619px;top:14px;width:489px;height:614px;border:3px solid #f3f1f3;box-shadow:0 4px 12px rgba(0,0,0,.2);background:linear-gradient(180deg,#3b4250 0%,#6b6f78 35%,#e2e2e4 60%,#4d5560 100%)}

/* Blog */
.blog{left:0;top:3348px;width:1200px;height:363px;background:#f4f4f5}
.blog h2{position:absolute;left:84px;top:60px}
.blog-card{top:140px;width:328px;height:153px;padding:22px 22px;box-shadow:0 3px 8px rgba(0,0,0,.12)}
.blog-card h5{font-size:15px;font-weight:600;color:#4a4a4d;line-height:1.45;margin-bottom:18px}
.blog-card span{font-size:14px;color:#5f5f64}
.blog-arrow{top:196px}

/* Contact */
.contact{left:0;top:3711px;width:1200px;height:419px;background:linear-gradient(180deg,#8d8d8f 0%,#b9b9bb 35%,#9d9d9f 60%,#6f7071 100%)}
.contact-circle{left:410px;top:33px;width:380px;height:380px;border-radius:50%;background:rgba(205,205,207,.85)}
.form{left:483px;top:120px;width:237px}
.field{height:30px;border:1px solid #707074;background:rgba(255,255,255,.25);font-size:10px;color:#7a7a7e;padding:7px 10px;margin-bottom:12px}
.field.message{height:62px}
.submit{height:42px;background:var(--btn-dark);color:#fff;font-size:10px;font-weight:500;text-align:center;line-height:42px;letter-spacing:.5px;margin-top:2px}

/* Footer */
.footer{left:0;top:4130px;width:1200px;height:56px;background:#fff;display:flex;align-items:center;justify-content:space-between;padding:0 88px;font-size:11px;color:var(--ink)}
.footer nav{display:flex;gap:22px}
</style>
</head>
<body>

<section class="abs hero">
  <div class="abs hero-ridge" role="img" aria-label="Photo of a woman meditating on a mountain top at sunset"></div>
  <div class="abs brand"><span class="brand-mark"></span>Tender Horizon</div>
  <div class="abs hero-circle"></div>
  <div class="abs hero-kicker">EXPERIENCE OUR</div>
  <div class="abs hero-title">KUNDALINI YOGA</div>
</section>

<nav class="abs menu">
  <div class="menu-close">X</div>
  <ul class="menu-list">
    <li>HOME PAGE</li>
    <li>ABOUT US</li>
    <li>OUR EVENTS</li>
    <li>OUR CLASSES</li>
    <li>OUR BLOG</li>
    <li>CONTACT US</li>
  </ul>
  <div class="menu-social"><span></span><span></span><span></span><span></span><span></span><span></span></div>
</nav>

<figure class="abs portrait">
  <div class="portrait-photo" role="img" aria-label="Portrait photo of the teacher wearing a white headband"></div>
  <figcaption class="portrait-caption">LENA (SAT HARI KAUR)</figcaption>
</figure>

<div class="abs feature" style="left:84px">
  <div class="feature-icon" style="background:var(--pink)"></div>
  <div>
    <h3>Kundalini Yoga</h3>
    <p>It's Yoga for everyone. Compared to many other types of yoga, Kundalini Yoga is characterized by</p>
  </div>
</div>
<div class="abs feature" style="left:790px">
  <div class="feature-icon" style="background:var(--lavender)"></div>
  <div>
    <h3>For your comfort.</h3>
    <p>Wear loose fitted clothing that is comfortable moves with you. You may wish to wear layers as your</p>
  </div>
</div>

<section class="abs intro">
  <div class="abs intro-photo" role="img" aria-label="Photo of the teacher seated cross-legged on a rug among pine trees"></div>
  <div class="abs intro-copy">
    <h2>Kundalini Yoga</h2>
    <p>Kundalini Yoga comes from northern India and has a centuries-long tradition. It was brought to the West in 1969. It is a powerful yoga system that includes not only physical and meditation exercises but also healing techniques such as Sat Nam Rasayan and yogic massage, nutrition and lifestyle teachings of Ayurveda, and yogic lifestyle. The comprehensive science of Kundalini Yoga also includes Numerology, the large group meditation courses of White Tantric Yoga, the martial arts technique Gatka, and special pregnancy yoga and yoga for children.</p>
    <p>Kundalini Yoga is also called the "Yoga of Awareness". It is ideal for people in the prime of their lives, because it helps to meet the daily demands and challenges actively while staying calm and balanced. The aim of this comprehensive self-training is the harmonization of body, mind and spirit through posture and movement, concentration, focus and meditation, conscious breathing and sound (mantra).</p>
  </div>
  <div class="abs wellbeing-photo" role="img" aria-label="Photo of the teacher in white with open palms in a snowy landscape"></div>
  <div class="abs wellbeing-copy">
    <h2>Your Wellbeing.</h2>
    <p>You are responsible to make me aware of any medical conditions or physical concerns you may have in general and on the day of your class. I will offer guidance and accommodations based on this knowledge. Chairs and props are available to assist you whenever you need them. It is your responsibility to keep yourself safe and injury free.</p>
    <p>Use your own wisdom and knowledge of your body to make adjustments during your practice. This is YOUR practice and is intended to serve and address your particular needs. You always have a choice. You decide what's right for you.</p>
    <span class="btn" style="margin-top:22px">Register For Classes</span>
  </div>
</section>

<section class="abs contribute">
  <div class="abs stack">
    <div class="stack-back one"></div>
    <div class="stack-back two"></div>
    <div class="stack-front" role="img" aria-label="Photo of four young girls in white dresses sitting on the grass"></div>
  </div>
  <div class="abs contribute-copy">
    <h2>You contribute to the experience.</h2>
    <p>Please refrain from wearing perfume or other strong scents to class. Turn off cell phones or make them completely silent. In other words no vibration. Remove shoes in the vestibule before entering the practice area. Be on time to class. If you intend to miss a class please email (tenderhorizonyoga@mail.com) or TEXT (555) 014-2288.</p>
    <span class="btn">Register For Classes</span>
  </div>
</section>

<section class="abs classes">
  <div class="abs classes-copy">
    <h2>Our Classes</h2>
    <p>A typical part of Kundalini Yoga is a dynamic or flowing exercise series, beside quiet posture-holding exercises and versatile meditations, which are often also applied to Mantra music. The energy is brought to flow. This can lead to greater vigor and more awareness in everyday life and a more conscious and healthy dealing with one self and others. Kundalini Yoga is not dogmatic, but impact-oriented, full of meditative elements and techniques that can be</p>
  </div>
  <ul class="abs class-list">
    <li class="class-item">
      <svg width="32" height="40" viewBox="0 0 32 40"><circle cx="16" cy="7" r="5" fill="#a58bb3"/><path d="M16 13 L6 32 H26 Z" fill="#a58bb3"/><rect x="2" y="32" width="28" height="4" rx="2" fill="#a58bb3"/></svg>
      <div><h4>SoftFlow Barre</h4><span>19/05/15 – 01:00pm – 03:00pm</span></div>
    </li>
    <li class="class-item">
      <svg width="32" height="40" viewBox="0 0 32 40"><circle cx="16" cy="7" r="5" fill="#a58bb3"/><path d="M16 13 L6 32 H26 Z" fill="#a58bb3"/><rect x="2" y="32" width="28" height="4" rx="2" fill="#a58bb3"/></svg>
      <div><h4>SoftFlow Core</h4><span>19/05/15 – 01:00pm – 03:00pm</span></div>
    </li>
    <li class="class-item">
      <svg width="32" height="40" viewBox="0 0 32 40"><circle cx="16" cy="7" r="5" fill="#a58bb3"/><path d="M16 13 L6 32 H26 Z" fill="#a58bb3"/><rect x="2" y="32" width="28" height="4" rx="2" fill="#a58bb3"/></svg>
      <div><h4>SoftFlow Core</h4><span>19/05/15 – 01:00pm – 03:00pm</span></div>
    </li>
  </ul>
  <div class="abs classes-photo" role="img" aria-label="Photo of the teacher in a headwrap meditating indoors beside plants"></div>
</section>

<section class="abs blog">
  <h2>Our Blog</h2>
  <svg class="abs blog-arrow" style="left:52px" width="18" height="30" viewBox="0 0 18 30"><path d="M15 3 L4 15 L15 27" fill="none" stroke="#3b3b3d" stroke-width="3"/></svg>
  <article class="abs blog-card" style="left:84px;background:var(--card-blue)">
    <h5>Contrary to popular belief, Lorem Ipsum random text.</h5>
    <span>24 Dec, Monday @ 08:00 am</span>
  </article>
  <article class="abs blog-card" style="left:436px;background:var(--card-pink)">
    <h5>Contrary to popular belief, Lorem Ipsum random text.</h5>
    <span>24 Dec, Monday @ 08:00 am</span>
  </article>
  <article class="abs blog-card" style="left:788px;background:var(--card-peach)">
    <h5>Contrary to popular belief, Lorem Ipsum random text.</h5>
    <span>24 Dec, Monday @ 08:00 am</span>
  </article>
  <svg class="abs blog-arrow" style="left:1126px" width="18" height="30" viewBox="0 0 18 30"><path d="M3 3 L14 15 L3 27" fill="none" stroke="#3b3b3d" stroke-width="3"/></svg>
</section>

<section class="abs contact" role="img" aria-label="Black and white photo of a woman sitting before a mountain landscape">
  <div class="abs contact-circle"></div>
  <form class="abs form">
    <div class="field">Name</div>
    <div class="field">Email Address</div>
    <div class="field message">Message</div>
    <div class="submit">SUBMIT</div>
  </form>
</section>

<footer class="abs footer">
  <span>© Copyright 2018 | All Rights Reserved.</span>
  <nav><span>Home</span><span>About</span><span>Events</span><span>Classes</span><span>Blog</span><span>Contact</span></nav>
</footer>

</body>
</html>
```